Landing page for B2B Product Idea Validation Event

We need a single landing page design for the world’s first competition to help aspiring entrepreneurs to validate their new business 2 business (B2B) web application ideas.

We like the following landing pages as examples for the structure and sectioning we would like to see for this landing page:
http://ny.brivolex.com/
https://tarvel.com/tarvelfest

There should be around 5 sections including an application form.

Target Market(s)

Entrepreneurs

Industry/Entity Type

Business Software

Number of Pages Required

1 page

Font styles to use
Serif

Requirements
Must have
• Colors must be similar to the logo provided.

```html
<!DOCTYPE html>
<html lang="en">
<head>
<meta charset="utf-8">
<title>Quenvalo – B2B Idea Validation Competition</title>
<link href="https://fonts.googleapis.com/css2?family=Roboto:wght@400;500;700&display=swap" rel="stylesheet">
<style>
  :root {
    --brand-navy: #1f4f91;
    --nav-blue: #0a8cd4;
    --hero-blue: #0d9fe6;
    --hero-deep: #0787cf;
    --card-blue: #0b8fd8;
    --card-grey: #9b9b9b;
    --card-coral: #fd5e48;
    --coral-fold: #fe9a8c;
    --button-coral: #fb5d49;
    --ink: #333333;
    --ink-soft: #444444;
    --rule: #9a9a9a;
    --footer-navy: #2c4b80;
    --white: #ffffff;
  }
  * { box-sizing: border-box; margin: 0; padding: 0; }
  html, body {
    width: 1147px;
    height: 1200px;
    overflow: hidden;
    background: var(--white);
    font-family: "Roboto", Arial, sans-serif;
    color: var(--ink);
  }
  .page { position: relative; width: 1147px; height: 1200px; }

  /* Header */
  .site-header { position: absolute; top: 0; left: 0; width: 100%; height: 88px; background: var(--white); }
  .brand { position: absolute; left: 115px; top: 27px; display: flex; align-items: center; gap: 10px; }
  .brand-mark { width: 30px; height: 30px; border-radius: 50%; background: var(--brand-navy); }
  .brand-name { font-size: 29px; font-weight: 500; color: var(--brand-navy); letter-spacing: -0.3px; }
  .phone { position: absolute; left: 681px; top: 34px; font-size: 17px; color: var(--ink); }
  .login { position: absolute; left: 889px; top: 36px; font-size: 14px; color: var(--nav-blue); display: flex; align-items: center; gap: 6px; text-decoration: none; }

  /* Navigation */
  .main-nav { position: absolute; top: 88px; left: 0; width: 100%; height: 75px; background: var(--nav-blue); }
  .main-nav a { position: absolute; top: 22px; font-size: 18px; color: var(--white); text-decoration: none; }
  .nav-active-line { position: absolute; left: 437px; top: 49px; width: 144px; height: 2px; background: var(--white); }
  .nav-active-tip { position: absolute; left: 503px; top: 43px; width: 0; height: 0;
    border-left: 6px solid transparent; border-right: 6px solid transparent; border-bottom: 6px solid var(--white); }

  /* Hero */
  .hero { position: absolute; top: 163px; left: 0; width: 100%; height: 260px;
    background: linear-gradient(120deg, var(--hero-deep) 0%, var(--hero-blue) 45%, #18a8ee 70%, var(--hero-deep) 100%); }
  .hero-visual { position: absolute; left: 300px; top: 4px; width: 236px; height: 190px; border-radius: 12px;
    background: radial-gradient(ellipse at center, #8fe0ff 0%, #45c4f2 35%, rgba(13,159,230,0) 72%); }
  .hero-copy { position: absolute; left: 619px; top: 42px; width: 460px; color: var(--white); }
  .hero-lead { font-size: 17.5px; line-height: 21.5px; }
  .hero-title { font-size: 22px; font-weight: 700; margin-top: 7px; }
  .button { display: inline-block; background: var(--button-coral); color: var(--white); font-weight: 700;
    font-size: 17px; text-align: center; text-decoration: none; box-shadow: 0 2px 0 rgba(0,0,0,0.15); }
  .hero .button { position: absolute; left: -1px; top: 124px; width: 158px; height: 37px; line-height: 37px; }

  /* Feature cards */
  .card { position: absolute; top: 474px; width: 246px; height: 296px; color: var(--white); padding: 16px 14px 0 25px; }
  .card-eligibility { left: 182px; background: var(--card-blue); }
  .card-process { left: 452px; background: var(--card-grey); }
  .card-prize { left: 722px; background: var(--card-coral); }
  .card h2 { font-size: 20px; font-weight: 700; line-height: 22px; margin-bottom: 6px; }
  .card ul { list-style: none; }
  .card li { font-size: 12px; font-weight: 700; line-height: 21.5px; }
  .card-process li { font-weight: 400; }
  .card-fold { position: absolute; right: 0; bottom: 0; width: 33px; height: 33px; }

  /* Details */
  .divider { position: absolute; left: 114px; top: 827px; width: 922px; height: 1px; background: var(--rule); }
  .column-rule { position: absolute; left: 575px; top: 846px; width: 1px; height: 259px; background: var(--rule); }
  .details { position: absolute; }
  .details h3 { font-size: 24px; font-weight: 400; color: var(--ink); margin-bottom: 10px; }
  .details p { font-size: 17px; line-height: 21.5px; color: var(--ink-soft); }
  .timeline { left: 198px; top: 874px; }
  .judges { left: 198px; top: 969px; }
  .application { left: 650px; top: 874px; }
  .application .button { position: absolute; left: 10px; top: 143px; width: 157px; height: 38px; line-height: 38px; }

  /* Footer */
  .site-footer { position: absolute; left: 0; top: 1153px; width: 100%; height: 47px; background: var(--footer-navy); color: var(--white); }
  .copyright { position: absolute; left: 183px; top: 16px; font-size: 13px; }
  .social { position: absolute; left: 862px; top: 14px; display: flex; gap: 14px; font-size: 13px; font-weight: 700; }
  .social a { color: var(--white); text-decoration: none; }
</style>
</head>
<body>
<div class="page">

  <header class="site-header">
    <div class="brand">
      <span class="brand-mark"></span>
      <span class="brand-name">Quenvalo</span>
    </div>
    <div class="phone">US: 1-888-555-0147</div>
    <a class="login" href="#">
      <svg width="13" height="14" viewBox="0 0 13 14" aria-hidden="true">
        <circle cx="6.5" cy="4" r="3.5" fill="#0a8cd4"/>
        <path d="M0 14 C0 9 3 8 6.5 8 C10 8 13 9 13 14 Z" fill="#0a8cd4"/>
      </svg>
      Login to my account
    </a>
  </header>

  <nav class="main-nav">
    <a href="#" style="left:427px">Products &amp; Solutions</a>
    <span class="nav-active-tip"></span>
    <span class="nav-active-line"></span>
    <a href="#" style="left:627px">Resources</a>
    <a href="#" style="left:747px">Support</a>
    <a href="#" style="left:845px">How it works</a>
    <a href="#" style="left:981px">About</a>
  </nav>

  <section class="hero">
    <div class="hero-visual" role="img" aria-label="Glowing cube illustration with software and server icons"></div>
    <div class="hero-copy">
      <p class="hero-lead">The world's first competition to help aspiring entrepreneurs to validate their new business 2 business (B2B) ideas</p>
      <p class="hero-title">Start Differently</p>
      <a class="button" href="#">Apply Now!</a>
    </div>
  </section>

  <section class="card card-eligibility">
    <h2>Eligibility</h2>
    <ul>
      <li>- Passionate Individual</li>
      <li>- Your idea is b2b solution (aka<br>&nbsp;&nbsp;selling to other businesses)</li>
      <li>- Your idea if validated would be<br>&nbsp;&nbsp;a SaaS product/company</li>
      <li>- You currently have visibility or<br>&nbsp;&nbsp;directly involved with a problem<br>&nbsp;&nbsp;in your industry and you believe<br>&nbsp;&nbsp;a software solution could be the<br>&nbsp;&nbsp;answer</li>
    </ul>
  </section>

  <section class="card card-process">
    <h2>Application and<br>Review Process</h2>
    <ul>
      <li>- Submissions will be reviewed by a<br>round 1 judging committee</li>
      <li>- Initial judging will limit the field to<br>20 ideas</li>
      <li>- These 20 ideas will be asked to<br>submit 10 minute pitch video on<br>their idea</li>
      <li>- These videos will be reviewed<br>round 2 judges they will select 10<br>winners</li>
    </ul>
  </section>

  <section class="card card-prize">
    <h2>Prize</h2>
    <ul>
      <li>- Proven Guided Validation</li>
      <li>- Process on your idea with<br>industry experts</li>
      <li>- Step by Step Process and tools<br>to validate your idea (aka our<br>coaching model)</li>
      <li>- 6 week process</li>
      <li>- Insider tips and tricks for<br>success</li>
      <li>- Accountability</li>
    </ul>
    <svg class="card-fold" viewBox="0 0 33 33" aria-hidden="true">
      <polygon points="33,0 33,33 0,33" fill="#ffffff"/>
      <polygon points="33,0 0,33 0,0" fill="#fe9a8c"/>
    </svg>
  </section>

  <div class="divider"></div>
  <div class="column-rule"></div>

  <section class="details timeline">
    <h3>Timeline</h3>
    <p>- Open Submissions: Early August</p>
    <p>- Close Round 1 Submissions: September 16th</p>
  </section>

  <section class="details judges">
    <h3>Judges/Mentors</h3>
    <p>- 7 judges</p>
    <p>- Bio</p>
    <p>- Headshot</p>
  </section>

  <section class="details application">
    <h3>Application Form</h3>
    <p>- Basic bio form</p>
    <p>- 7 questions</p>
    <p>- 5 openended</p>
    <p>- 2 yes/no</p>
    <a class="button" href="#">Apply Now!</a>
  </section>

  <footer class="site-footer">
    <div class="copyright">Copyright © 2016 Quenvalo</div>
    <div class="social">
      <a href="#">Linkora</a>
      <a href="#">Plusio</a>
      <a href="#">Chirpa</a>
    </div>
  </footer>

</div>
</body>
</html>
```